KTR Engineering Pty Ltd

I have already had Corvale welding and fabrication cards made , my business has changed too KTR engineering Pty Ltd so I need my logo changed on the cards
one side have my logo then the other side have what we do.
front side logo and details
owner /operator : Lachlan Meravic
email: ktr.works@ironvalemail.com
number: 0491537204
ABN: 47 261 538 902
ACN: 718 352 946
on back have in dot points what we do:
* structural steel erection
* precast panels
* site welding
*steel alteration & repair
* rigging & dogging
*labour hire
all details in breif

```html
<!DOCTYPE html>
<html lang="en">
<head>
<meta charset="utf-8">
<title>KTR Engineering Pty Ltd – Business Cards</title>
<link rel="stylesheet" href="https://fonts.googleapis.com/css2?family=Open+Sans:wght@400;600;700;800&display=swap">
<style>
  :root {
    --backdrop: #232323;
    --card: #1b2230;
    --card-deep: #141a25;
    --pattern-hi: #2a3446;
    --accent: #a3413a;
    --ink: #ffffff;
    --ghost: #232c3c;
  }
  * { margin: 0; padding: 0; box-sizing: border-box; }
  html, body {
    width: 1200px; height: 780px; overflow: hidden;
    background: var(--backdrop);
    font-family: "Open Sans", Arial, sans-serif;
  }
  .sheet {
    width: 1200px; height: 780px;
    display: flex; align-items: center; justify-content: center; gap: 36px;
  }
  .card {
    position: relative;
    width: 540px; height: 310px;
    background: var(--card);
    overflow: hidden;
    box-shadow: 0 14px 30px rgba(0,0,0,.45);
  }

  /* Back: brand pattern side */
  .brand-pattern {
    position: absolute; inset: 0;
    background: linear-gradient(200deg, var(--pattern-hi) 0%, var(--card) 45%, var(--card-deep) 100%);
  }
  .back-mark {
    position: absolute; right: 40px; bottom: 44px;
    color: var(--ink); font-weight: 700; font-size: 11px;
    letter-spacing: .3px;
  }

  /* Front: details side */
  .company-mark {
    position: absolute; left: 34px; top: 40px;
    color: var(--ink); font-weight: 800; font-size: 19px;
    line-height: 1.15; width: 200px;
  }
  .ghost-mark {
    position: absolute; right: 22px; bottom: 26px;
    color: var(--ghost); font-weight: 800; font-size: 40px;
    line-height: 1; text-align: right; width: 260px;
  }
  .person {
    position: absolute; left: 34px; top: 128px;
    padding-left: 16px;
    border-left: 8px solid var(--accent);
  }
  .person-name { font-size: 27px; font-weight: 700; color: var(--ink); line-height: 1.1; }
  .person-name .first { color: var(--accent); }
  .person-role { font-size: 13px; color: var(--ink); margin-top: 2px; }
  .registry {
    position: absolute; left: 58px; top: 200px;
    font-size: 13px; color: var(--ink); line-height: 1.45;
  }
  .registry .label { color: var(--accent); }
  .contact {
    position: absolute; left: 58px; top: 246px;
    font-size: 13px; color: var(--ink); line-height: 1.5;
    list-style: none;
  }
  .contact li { display: flex; align-items: center; gap: 8px; }
  .contact svg { width: 13px; height: 13px; flex: none; }
  .services {
    position: absolute; right: 26px; top: 34px;
    text-align: right; list-style: none;
    font-size: 12.5px; color: var(--ink); line-height: 1.55;
  }
  .services-title { color: var(--accent); font-size: 13px; letter-spacing: .3px; }
  .services li { display: flex; align-items: center; justify-content: flex-end; gap: 8px; }
  .services li::after {
    content: ""; width: 7px; height: 7px; border-radius: 50%;
    background: var(--accent); flex: none;
  }
  .services li.services-title::after { content: none; }
</style>
</head>
<body>
<main class="sheet">
  <section class="card card--back">
    <div class="brand-pattern" role="img" aria-label="Repeating company name pattern fading across the card"></div>
    <div class="back-mark">KTR Engineering Pty Ltd</div>
  </section>

  <section class="card card--front">
    <div class="ghost-mark">KTR Engineering Pty Ltd</div>
    <div class="company-mark">KTR Engineering Pty Ltd</div>

    <div class="person">
      <div class="person-name"><span class="first">Lachlan</span> Meravic</div>
      <div class="person-role">owner /operator</div>
    </div>

    <div class="registry">
      <div><span class="label">ABN:</span> 47 261 538 902</div>
      <div><span class="label">ACN:</span> 718 352 946</div>
    </div>

    <ul class="contact">
      <li>
        <svg viewBox="0 0 24 24" aria-hidden="true"><path fill="#a3413a" d="M6.6 10.8a15.1 15.1 0 0 0 6.6 6.6l2.2-2.2a1 1 0 0 1 1-.25 11.4 11.4 0 0 0 3.6.57 1 1 0 0 1 1 1V20a1 1 0 0 1-1 1A17 17 0 0 1 3 4a1 1 0 0 1 1-1h3.5a1 1 0 0 1 1 1c0 1.25.2 2.45.57 3.6a1 1 0 0 1-.25 1z"/></svg>
        0491537204
      </li>
      <li>
        <svg viewBox="0 0 24 24" aria-hidden="true"><path fill="#a3413a" d="M3 5h18a1 1 0 0 1 1 1v12a1 1 0 0 1-1 1H3a1 1 0 0 1-1-1V6a1 1 0 0 1 1-1zm9 7.2L4.2 7v1.9L12 14l7.8-5.1V7z"/></svg>
        ktr.works@ironvalemail.com
      </li>
    </ul>

    <ul class="services">
      <li class="services-title">WHAT WE DO</li>
      <li>Site welding</li>
      <li>Labour hire</li>
      <li>Precast panels</li>
      <li>Rigging &amp; dogging</li>
      <li>Structural steel erection</li>
      <li>Steel alteration &amp; repair</li>
    </ul>
  </section>
</main>
</body>
</html>
```